Wordpress Website for Kestrel Path Youth Support Initiative

We are looking for a wordpress website that is clean, crisp and bold for our Kestrel Path Youth Support Initiative.

We are a Canadian hospital in Winnipeg, MB which sees many youth injured by violence. We are starting up an Kestrel Path Youth Support Initiative for youth injured by violence. The youth who we will serve will be between the age of 14 - 24 and many will be gang-involved.

However, it is important to note that this website isn't for the youth themselves as much as it is for professionals and community interested in learning about our program. As such, it is should be friendly but professional. I am interested in a bold, crisp look.

I have attached our logo file for your use.
Updates

I forgot to mention that there should be a section along the bottom to include logos of funders and partners.

Also would be nice to include a spot for viewers to automatically subscribe to our newsletter by putting their email in.

I have added in a file of text that I will use - but want to easily be able to change and update (and post links etc). 

Target Market(s)

This will target a professional and community audience. We would like a crisp, bold, professional presence

Industry/Entity Type

Hospital

Requirements
Must have
• I would like a navigation bar that includes the following:

About KP-YSI (Background and Research sections)
People
Latest News
Job Opportunities
Research Opportunities
Publications & Reports
Contact KP-YSI ( a form)

I would also like a search form and a link to plimzo.

While I am comfortable with Wordpress - I am not an expert. I want this to be as simple as possible for me to update.
Nice to have
• We have a great logo and only a few photos which I will upload in the next day.

We could also use stock photos for now but overtime switch these with photos of our own hospital emergency department and team. Additionally, we would like some stock photos of youth - a diverse mix but to include Aboriginal/First Nations, immigrant and caucasian youth
Should not have
• This design should not have guns, knifes, alcohol or blood/gore in there (I've learned to state this after using pixel harbor for the logo! )

```html
<!DOCTYPE html>
<html lang="en">
<head>
<meta charset="utf-8">
<title>Kestrel Path Youth Support Initiative</title>
<link href="https://fonts.googleapis.com/css2?family=Ubuntu:wght@300;400;500;700&display=swap" rel="stylesheet">
<style>
:root{
  --brand:#8e1f22;
  --brand-dark:#6e1417;
  --nav-top:#a8353a;
  --nav-bottom:#8a1f23;
  --heading:#3a3a3a;
  --text:#333;
  --muted:#8a8a8a;
  --blush:#f1e2e2;
  --rule:#e4e4e4;
  --footer:#f3f3f3;
  --base:#ececec;
}
*{margin:0;padding:0;box-sizing:border-box}
html,body{width:1087px;height:1200px;overflow:hidden;background:#fff}
body{position:relative;font-family:'Ubuntu',sans-serif;color:var(--text)}
.abs{position:absolute}
.top-band{left:0;top:0;width:1087px;height:317px;background:linear-gradient(#fbf6f6,var(--blush))}
.brand-mark{left:85px;top:26px;font-weight:700;font-size:36px;color:var(--brand);letter-spacing:-1px;line-height:36px;width:80px}
.brand-name{left:176px;top:24px;font-size:13px;font-weight:300;color:#555;line-height:14.6px;padding-left:8px;border-left:1px solid #ccc}
.social{left:729px;top:75px;display:flex;gap:3px}
.social span{width:24px;height:24px;border-radius:50%;background:var(--brand);color:#fff;font-size:13px;font-weight:500;display:flex;align-items:center;justify-content:center;line-height:1}
.support{left:856px;top:53px;font-size:18px;font-weight:300;color:#666}
.phone{left:856px;top:74px;font-size:23px;color:#444}
.main-nav{left:75px;top:112px;width:936px;height:46px;display:flex;background:linear-gradient(var(--nav-top),var(--nav-bottom));border-radius:3px 3px 0 0}
.main-nav a{color:#fff;text-decoration:none;font-size:15px;display:flex;align-items:center;justify-content:center;border-right:1px solid rgba(0,0,0,.18);box-shadow:1px 0 0 rgba(255,255,255,.12)}
.main-nav a:last-child{border-right:0;box-shadow:none}
.hero{left:75px;top:158px;width:936px;height:333px;background:linear-gradient(160deg,#c9d6e4 0%,#e8ecef 35%,#c23a3e 55%,#f1eeea 70%,#b9c7d6 100%);border:1px solid #ddd}
.arrow{top:288px}
h1.welcome{left:77px;top:512px;font-size:25px;font-weight:400;color:var(--heading)}
.lead{left:79px;top:551px;width:420px;font-size:13px;line-height:19px;color:#333}
.body-copy{left:79px;top:597px;width:420px;font-size:12px;line-height:19px;font-weight:300;color:var(--muted)}
.body-copy p+p{margin-top:10px}
.feature{top:516px;width:225px}
.feature h2{font-size:21px;font-weight:400;color:var(--brand);margin-bottom:10px}
.feature .photo{height:102px;background:linear-gradient(120deg,#e7eef2,#cdd6dc 60%,#a9b3ba)}
.feature .photo.ambulance{background:linear-gradient(120deg,#5d6873,#b9c2cb 50%,#2f3b4f)}
.feature h3{font-size:15px;font-weight:400;color:#333;margin:10px 0 4px 1px}
.feature p{font-size:11.4px;line-height:19px;font-weight:300;color:var(--muted);margin-left:1px}
.rule{left:76px;top:777px;width:912px;height:1px;background:var(--rule)}
.partner{top:812px;height:52px;border-radius:4px}
.footer{left:0;top:912px;width:1087px;height:232px;background:linear-gradient(var(--footer),#fff 40%)}
.col{top:959px}
.col h4{font-size:18px;font-weight:400;color:#444;margin-bottom:12px}
.col ul{list-style:none}
.col li{font-size:13px;font-weight:300;color:#444;line-height:24.6px;margin-left:2px}
.subscribe-note{font-size:14px;font-weight:300;color:#444;margin:-2px 0 8px 1px}
.email{display:block;width:218px;height:29px;border:1px solid #ccc;border-radius:2px;background:#fff;font:300 11px 'Ubuntu',sans-serif;color:#444;padding-left:12px;line-height:27px}
.subscribe-btn{position:absolute;left:118px;top:94px;width:101px;height:34px;background:linear-gradient(#d43a3a,#a81b1e);color:#fff;border-radius:3px;font-size:14px;display:flex;align-items:center;justify-content:center}
.base{left:0;top:1144px;width:1087px;height:56px;background:var(--base)}
.copyright{left:71px;top:1164px;font-size:12px;font-weight:300;color:#555}
</style>
</head>
<body>
<div class="abs top-band"></div>

<header>
  <div class="abs brand-mark">KP-<br>YSI</div>
  <div class="abs brand-name">Kestrel<br>Path<br>Youth<br>Support<br>Initiative</div>
  <div class="abs social" aria-label="Social links">
    <span aria-label="nestly">n</span><span aria-label="plimzo">p</span><span aria-label="kindra">k</span><span aria-label="vellum">v</span>
  </div>
  <div class="abs support">24/7 Support</div>
  <div class="abs phone">555-014-2270</div>
  <nav class="abs main-nav">
    <a style="width:80px">Home</a>
    <a style="width:72px">About</a>
    <a style="width:76px">People</a>
    <a style="width:110px">Latest News</a>
    <a style="width:148px">Job Opportunities</a>
    <a style="width:182px">Research Opportunities</a>
    <a style="width:172px">Publications &amp; Reports</a>
    <a style="width:96px">Contact</a>
  </nav>
</header>

<div class="abs hero" role="img" aria-label="Photo of a cheering crowd waving flags outdoors"></div>
<svg class="abs arrow" style="left:90px" width="34" height="62" viewBox="0 0 34 62"><polyline points="30,2 4,31 30,60" fill="none" stroke="#111" stroke-width="5"/></svg>
<svg class="abs arrow" style="left:962px" width="34" height="62" viewBox="0 0 34 62"><polyline points="4,2 30,31 4,60" fill="none" stroke="#111" stroke-width="5"/></svg>

<main>
  <h1 class="abs welcome">Welcome to Our Website Mainpage</h1>
  <p class="abs lead">Pellentesque habitant morbi tristique senectus et netus et malesuada fames ac turpis egestas. In posuere felis nec tortor.</p>
  <div class="abs body-copy">
    <p>Pellentesque faucibus. Ut accumsan ultricies elit. Maecenas at justo id velit placerat molestie. Donec dictum lectus non odio. Cras a ante vitae enim iaculis aliquam. Mauris nunc quam, venenatis nec, euismod sit amet, egestas placerat, est. Pellentesque habitant morbi tristique senectus et netus et malesuada fames ac turpis egestas. Cras id elit. Integer quis urna.</p>
    <p>Mauris vel lacus vitae felis vestibulum volutpat.</p>
  </div>

  <section class="abs feature" style="left:535px">
    <h2>Services We Provide</h2>
    <div class="photo" role="img" aria-label="Photo of a doctor with a patient wearing a neck brace"></div>
    <h3>Ut accumsan ultricies elit</h3>
    <p>Maecenas at justo id velit placerat molestie. Donec dictum lectus non odio. Cras a ante vitae enim iaculis aliquam.</p>
  </section>
  <section class="abs feature" style="left:786px">
    <h2>Publications &amp; Reports</h2>
    <div class="photo ambulance" role="img" aria-label="Photo of paramedics attending a patient on a stretcher"></div>
    <h3>Ut accumsan ultricies elit</h3>
    <p>Maecenas at justo id velit placerat molestie. Donec dictum lectus non odio. Cras a ante vitae enim iaculis aliquam.</p>
  </section>

  <div class="abs rule"></div>

  <div aria-label="Funders and partners">
    <div class="abs partner" style="left:105px;width:52px;border-radius:50%;background:#cfe3cf"></div>
    <div class="abs partner" style="left:220px;width:98px;background:#ececec"></div>
    <div class="abs partner" style="left:360px;width:91px;background:#f2dcdc"></div>
    <div class="abs partner" style="left:471px;width:85px;background:#dde3f0"></div>
    <div class="abs partner" style="left:593px;width:116px;background:#d9deef"></div>
    <div class="abs partner" style="left:733px;width:106px;background:#e6e4ef"></div>
    <div class="abs partner" style="left:861px;width:126px;background:#d7e8dd"></div>
  </div>
</main>

<footer>
  <div class="abs footer"></div>
  <div class="abs col" style="left:68px">
    <h4>Quick Links</h4>
    <ul><li>Home</li><li>About &nbsp;Us</li><li>People</li><li>Latest News</li></ul>
  </div>
  <div class="abs col" style="left:219px">
    <h4>Sub Links</h4>
    <ul><li>Job Opportunities</li><li>Research Opportunities</li><li>Publications &amp; Reports</li><li>FAQ</li></ul>
  </div>
  <div class="abs col" style="left:411px">
    <h4>Support &amp; Contact</h4>
    <ul><li>Support</li><li>How we Help</li><li>Career</li><li>Contact</li></ul>
  </div>
  <div class="abs col" style="left:619px">
    <h4>Newsletters Subscribe</h4>
    <p class="subscribe-note">Please subscribe here for latest news</p>
    <span class="email">email address</span>
    <span class="subscribe-btn">SUBSCRIBE</span>
  </div>
  <div class="abs base"></div>
  <p class="abs copyright">© 2013 Company Name. &nbsp;All right reserved. &nbsp;Term of Use</p>
</footer>
</body>
</html>
```